Tovrell Family Reunion Flyer

A flyer detailing family reunion events. It should be complimentary to the logo style and fonts. BE DIFFERENT AVOID TEMPLATES

The 2015 Tovrell Family Reunion
Descendants of Besoda Nwaruk Felim Tovrell

Friday August 14th 2pm
Jummah Prayer At Suravan Mosque
Followed by Family Get Together

Saturday august 15th 12pm
Family Reunion Picnic
4127 tovrell Dr.
bowie

Hosted by the Children of The Prestigious Tovrell Family

Industry/Entity Type

Events

Colors
0355a3
9bcb3c

Requirements
Must have
• Logo

```html
<!DOCTYPE html>
<html lang="en">
<head>
<meta charset="utf-8">
<title>Tovrell Family Reunion 2015</title>
<link rel="stylesheet" href="https://fonts.googleapis.com/css2?family=Montserrat:wght@500;700;800;900&family=Staatliches&display=swap">
<style>
  :root {
    --green: #2c7a3c;
    --blue: #5b9bd0;
    --ink: #151515;
    --paper: #ffffff;
  }
  * { margin: 0; padding: 0; box-sizing: border-box; }
  html, body { width: 922px; height: 1200px; overflow: hidden; background: var(--paper); }
  .flyer {
    position: relative;
    width: 922px;
    height: 1200px;
    background: var(--paper);
    font-family: "Montserrat", Arial, sans-serif;
    color: var(--ink);
  }
  .rule { position: absolute; left: 0; width: 922px; height: 4px; background: var(--blue); }
  .rule--top { top: 2px; }
  .rule--bottom { top: 49px; }
  .lineage {
    position: absolute; top: 10px; left: 0; width: 922px;
    text-align: center; font-weight: 700; font-size: 28px; letter-spacing: 0.2px;
  }
  .emblem { position: absolute; left: 296px; top: 110px; width: 330px; height: 330px; }
  .emblem-name {
    position: absolute; top: 478px; left: 0; width: 922px; text-align: center;
    font-weight: 700; font-size: 24px; color: var(--green);
  }
  .schedule { position: absolute; left: 0; top: 560px; width: 922px; height: 270px; }
  .schedule text { font-family: "Montserrat", Arial, sans-serif; }
  .event-time { font-weight: 800; font-size: 30px; fill: var(--green); }
  .event-day, .event-month { font-weight: 800; fill: var(--ink); }
  .event-day { font-size: 46px; }
  .event-month { font-size: 60px; }
  .event-num { font-weight: 800; font-size: 46px; fill: var(--blue); }
  .event-detail { font-weight: 700; font-size: 13px; fill: var(--ink); }
  .invite { position: absolute; left: 0; top: 850px; width: 922px; height: 250px; }
  .host {
    position: absolute; top: 1150px; left: 0; width: 922px; text-align: center;
    font-family: "Staatliches", Impact, sans-serif; font-size: 30px; letter-spacing: 0.5px;
  }
</style>
</head>
<body>
<main class="flyer">
  <div class="rule rule--top"></div>
  <h1 class="lineage">Descendants of Besoda Nwaruk Felim Tovrell</h1>
  <div class="rule rule--bottom"></div>

  <svg class="emblem" viewBox="0 0 330 330" role="img" aria-label="Tovrell Family Reunion emblem">
    <circle cx="165" cy="165" r="158" fill="none" stroke="var(--green)" stroke-width="6"/>
  </svg>
  <p class="emblem-name">Tovrell Family Reunion 2015</p>

  <svg class="schedule" viewBox="0 0 922 270">
    <g class="event event--friday">
      <text class="event-time" x="201" y="63" text-anchor="middle" textLength="82" lengthAdjust="spacingAndGlyphs" transform="rotate(-90 201 63)">2PM</text>
      <text class="event-day" x="208" y="54" textLength="192" lengthAdjust="spacingAndGlyphs">FRIDAY</text>
      <text class="event-num" x="402" y="54" textLength="56" lengthAdjust="spacingAndGlyphs">14</text>
      <text class="event-month" x="208" y="102" textLength="250" lengthAdjust="spacingAndGlyphs">AUGUST</text>
      <text class="event-detail" x="507" y="56">Jummah Prayer At Suravan Mosque</text>
      <text class="event-detail" x="507" y="74">Followed by Family Get Together</text>
    </g>
    <g class="event event--saturday">
      <text class="event-time" x="201" y="209" text-anchor="middle" textLength="86" lengthAdjust="spacingAndGlyphs" transform="rotate(-90 201 209)">12PM</text>
      <text class="event-day" x="208" y="200" textLength="217" lengthAdjust="spacingAndGlyphs">SATURDAY</text>
      <text class="event-num" x="427" y="200" textLength="31" lengthAdjust="spacingAndGlyphs">15</text>
      <text class="event-month" x="208" y="249" textLength="250" lengthAdjust="spacingAndGlyphs">AUGUST</text>
      <text class="event-detail" x="507" y="201">Family Reunion Picnic</text>
      <text class="event-detail" x="507" y="220">4127 Tovrell Dr. Bowie</text>
    </g>
  </svg>

  <svg class="invite" viewBox="0 0 922 250">
    <text x="458" y="108" text-anchor="middle" textLength="678" lengthAdjust="spacingAndGlyphs"
          font-family="Montserrat, Arial, sans-serif" font-weight="900" font-size="132" fill="var(--green)">YOU ARE</text>
    <text x="455" y="238" text-anchor="middle" textLength="684" lengthAdjust="spacingAndGlyphs"
          font-family="Montserrat, Arial, sans-serif" font-weight="500" font-size="150"
          fill="var(--blue)" stroke="var(--blue)" stroke-width="10" stroke-linejoin="round">INVITED!</text>
    <text x="455" y="238" text-anchor="middle" textLength="684" lengthAdjust="spacingAndGlyphs"
          font-family="Montserrat, Arial, sans-serif" font-weight="500" font-size="150"
          fill="var(--paper)">INVITED!</text>
  </svg>

  <p class="host">Hosted by the children of the prestigious Tovrell family</p>
</main>
</body>
</html>
```